amber lanterns

We are in need of a website for married spouses or wives that are looking for a one night stand or affair, trying to get out from their marriage routine. We want our website for married people only.

i have extended my deadline until the 29 of april. we are looking for at least 8 pages if possible, but we would only like to see the first page as an example for the next few pages. if we really like your design we weill hire you and thenĀ  we talk about the rest of the pages and the money. if you have any comments or questions, don't be afraid to ask.

• We want to be able to have a link open to a future website. it needs pop ups and ads. we would like it to say at the bottom of the page, bolded and highlighted that, " We are not responsible for any sexually transmitted diseases" and " We are not responsible for any marriage break-ups or any problems in consequence after the encounters." " It is the responsibility of the subscriber(member) to have enough information about the person before the encounter." We would like the website to be compatible to fundora. The subscribers must be able to web chat, upload photos, and upload videos but can decide who can see them or watch them.They can also have the choice to block certain members from their profile.

```html
<!DOCTYPE html>
<html lang="en">
<head>
<meta charset="utf-8">
<title>Amber Lanterns</title>
<link href="https://fonts.googleapis.com/css2?family=Cabin:wght@500;600;700&family=Arimo:wght@400;700&display=swap" rel="stylesheet">
<style>
:root{
  --brown:#a86f45;
  --brown-dark:#7a4a2c;
  --brown-text:#8a4f2f;
  --ink:#3c3c3c;
  --body:#444;
  --peach-top:#fdf5ec;
  --peach-bottom:#f3c88c;
  --cream:#f9e8d2;
  --footer:#c3c3c3;
  --footer-text:#555;
  --white:#fff;
}
*{margin:0;padding:0;box-sizing:border-box}
html,body{width:993px;height:1200px;overflow:hidden}
body{font-family:"Arimo",Arial,sans-serif;color:var(--body);background:var(--footer);position:relative}
.abs{position:absolute}
.top-band{left:0;top:0;width:993px;height:571px;background:linear-gradient(var(--peach-top),#f8e2c4 40%,var(--peach-bottom));border-bottom:1px solid #b59a7e}
.brand{left:118px;top:16px;font-family:"Cabin",sans-serif;font-weight:700;font-size:33px;color:var(--brown-dark);letter-spacing:.5px}
.advert{left:462px;top:11px;width:428px;height:50px;border:1px solid #d8d0c6;border-radius:4px;background:rgba(255,255,255,.5);font-size:18px;color:#a8a8a8;display:flex;align-items:center;justify-content:center}
.nav{left:100px;top:73px;width:794px;height:35px;border-radius:8px 8px 0 0;background:linear-gradient(#bd845a,var(--brown-dark));display:flex;align-items:center}
.nav a{font-family:"Cabin",sans-serif;font-weight:700;font-size:14px;color:var(--white);text-decoration:none;display:flex;align-items:center;gap:6px;height:100%;padding:0 16px;border-right:1px solid rgba(255,255,255,.15)}
.nav a:last-child{border-right:0}
.nav a.active{color:#f6cf9c}
.chev{width:11px;height:11px;border-radius:50%;background:#8a5a3b;display:inline-flex;align-items:center;justify-content:center}
.hero{left:100px;top:112px;width:794px;height:252px;background:linear-gradient(180deg,#8d7355 0%,#c9ab85 35%,#a58a67 62%,#c8a57a 100%);box-shadow:0 10px 14px -8px rgba(0,0,0,.35)}
.hero-title{left:514px;top:72px;font-family:"Cabin",sans-serif;font-weight:600;font-size:23px;line-height:27px;color:#333}
.hero-btn{left:510px;top:131px;height:29px;padding:0 14px 0 9px;border-radius:4px;background:linear-gradient(#b27a52,var(--brown-dark));color:var(--white);font-family:"Cabin",sans-serif;font-weight:700;font-size:14px;display:flex;align-items:center;gap:12px}
.dots{left:468px;top:372px;display:flex;gap:3px}
.dots span{width:11px;height:11px;border-radius:50%;border:1px solid #8a6a4a;background:#fff8ee}
.dots span:first-child{background:#d9c2a2}
.members-title{left:107px;top:399px;font-family:"Cabin",sans-serif;font-size:20px;font-weight:700;color:#333}
.members-title b{color:var(--brown-text)}
.members{left:108px;top:431px;display:flex;gap:7px}
.member{width:72px;font-size:10px;line-height:13px;color:#333}
.member .ph{width:72px;height:71px;border:1px solid #fff;margin-bottom:9px}
.member b{display:block}
.content{left:0;top:571px;width:993px;height:290px;background:var(--cream)}
.col{top:46px;font-size:9.5px;line-height:12.8px;color:#444}
.col h2{font-family:"Cabin",sans-serif;font-weight:600;font-size:21px;color:#444;margin-bottom:4px;line-height:24px}
.col p{margin-bottom:13px}
.date{font-family:"Cabin",sans-serif;font-weight:600;font-size:10px;color:#7a6a5a;margin-bottom:3px}
.steps{list-style:none;font-size:12px;line-height:22px;color:#444;margin-top:8px}
.steps li{display:flex;align-items:center;gap:14px}
.steps .chev{width:16px;height:16px}
.btn{height:29px;width:119px;border-radius:4px;background:linear-gradient(#b57c53,var(--brown-dark));color:var(--white);font-family:"Cabin",sans-serif;font-weight:700;font-size:14px;display:flex;align-items:center;padding-left:9px;gap:11px;top:213px}
.disclaimer{left:0;top:861px;width:993px;height:106px;background:var(--brown);color:var(--white);font-weight:700;font-size:16.4px;line-height:23px;padding:13px 100px 0 104px}
.fcol{top:1022px;width:125px}
.fcol h3{font-family:"Cabin",sans-serif;font-weight:600;font-size:20px;color:#666;margin-bottom:6px}
.fcol a{display:block;font-size:11px;color:var(--footer-text);text-decoration:none;height:31.5px;border-bottom:1px solid #d6d6d6;padding-top:3px}
.social{left:730px;top:1031px;display:flex;gap:4px}
.social span{width:29px;height:29px;border-radius:4px;background:linear-gradient(#ececec,#d0d0d0);border:1px solid #bbb}
.fbrand{left:682px;top:1082px;font-family:"Cabin",sans-serif;font-weight:700;font-size:28px;color:#7a6a5e}
.copy{left:685px;top:1122px;font-size:11.5px;color:#444}
</style>
</head>
<body>
<div class="abs top-band"></div>
<div class="abs brand">Amber Lanterns</div>
<div class="abs advert">&lt;&lt; Place advert here &gt;&gt;</div>

<nav class="abs nav">
  <a class="active" href="#">HOME <span class="chev"><svg width="6" height="6" viewBox="0 0 6 6"><path d="M2 1l2 2-2 2" stroke="#fff" stroke-width="1.2" fill="none"/></svg></span></a>
  <a href="#">YOUR ACCOUNT <span class="chev"><svg width="6" height="6" viewBox="0 0 6 6"><path d="M2 1l2 2-2 2" stroke="#fff" stroke-width="1.2" fill="none"/></svg></span></a>
  <a href="#">JOIN <span class="chev"><svg width="6" height="6" viewBox="0 0 6 6"><path d="M2 1l2 2-2 2" stroke="#fff" stroke-width="1.2" fill="none"/></svg></span></a>
  <a href="#">BLOG <span class="chev"><svg width="6" height="6" viewBox="0 0 6 6"><path d="M2 1l2 2-2 2" stroke="#fff" stroke-width="1.2" fill="none"/></svg></span></a>
  <a href="#">CONTACT <span class="chev"><svg width="6" height="6" viewBox="0 0 6 6"><path d="M2 1l2 2-2 2" stroke="#fff" stroke-width="1.2" fill="none"/></svg></span></a>
  <a href="#">CREATE NEW ACCOUNT</a>
</nav>

<section class="abs hero" role="img" aria-label="Photo of a couple walking hand in hand on a beach at sunset">
  <h1 class="abs hero-title">Looking for a one<br>night stand or affair?</h1>
  <div class="abs hero-btn">START CONNECTING NOW <span class="chev" style="width:18px;height:18px;background:#8a5a3b"><svg width="8" height="8" viewBox="0 0 6 6"><path d="M2 1l2 2-2 2" stroke="#fff" stroke-width="1.2" fill="none"/></svg></span></div>
</section>
<div class="abs dots"><span></span><span></span><span></span><span></span></div>

<h2 class="abs members-title"><b>MEMBERS</b> online now:</h2>
<div class="abs members">
  <div class="member"><div class="ph" role="img" aria-label="Member photo" style="background:linear-gradient(#e8e2da,#b9a08a)"></div>John Graham<b>43 years</b></div>
  <div class="member"><div class="ph" role="img" aria-label="Member photo" style="background:linear-gradient(#ddd3c6,#b88d60)"></div>Joy Aaron<b>38 years</b></div>
  <div class="member"><div class="ph" role="img" aria-label="Member photo" style="background:linear-gradient(#9aa98a,#c8926a)"></div>Wilson White<b>36 years</b></div>
  <div class="member"><div class="ph" role="img" aria-label="Member photo" style="background:linear-gradient(#f2f2f2,#8a7a70)"></div>Fredrick Lukas<b>40 years</b></div>
  <div class="member"><div class="ph" role="img" aria-label="Member photo" style="background:linear-gradient(#f7f4f0,#e2c8b4)"></div>Mary Johnson<b>31 years</b></div>
  <div class="member"><div class="ph" role="img" aria-label="Member photo" style="background:linear-gradient(#d7b68a,#a87a52)"></div>Steve Wright<b>36 years</b></div>
  <div class="member"><div class="ph" role="img" aria-label="Member photo" style="background:linear-gradient(#eee9e4,#c9a48a)"></div>Mike Lubrons<b>38 years</b></div>
  <div class="member"><div class="ph" role="img" aria-label="Member photo" style="background:linear-gradient(#8a6a58,#d1a88c)"></div>Stella Bright<b>32 years</b></div>
  <div class="member"><div class="ph" role="img" aria-label="Member photo" style="background:linear-gradient(#ececec,#b89c88)"></div>Debroah Wilks<b>28 years</b></div>
  <div class="member"><div class="ph" role="img" aria-label="Member photo" style="background:linear-gradient(#e6e6e6,#7a5a48)"></div>Larry Wilson<b>39 years</b></div>
</div>

<main class="abs content">
  <div class="abs col" style="left:104px;width:280px">
    <h2 style="margin-left:3px">WELCOME</h2>
    <p>Lorem ipsum dolor sit amet, consectetuer adipiscing elit. Praesent vestibulum molestie lacus. Aenean nonum hendrerit</p>
    <p>Nascetur ridiculus mus. Nulla dui. Fusce feugiat malesuada odio. Morbi nunc odio, gravida at, cursus nec, luctus a, lorem. Maecenas tristique orci sem. Duis ultricies pharetra magna. Donec accumsan malesuada orci. Donec sit amet eros. Lorem ipsum dolor sit amet, consectetuer adipiscing elit.</p>
  </div>
  <div class="abs col" style="left:424px;width:210px">
    <h2>DON´T Stay Alone</h2>
    <p>Nascetur ridiculus mus. Nulla dui. Fusce feugiat malesuada odio. Morbi nunc odio, gravida at, cursus nec, luctus a, lorem:</p>
    <ul class="steps">
      <li><span class="chev"><svg width="7" height="7" viewBox="0 0 6 6"><path d="M2 1l2 2-2 2" stroke="#fff" stroke-width="1.3" fill="none"/></svg></span>Register Now</li>
      <li><span class="chev"><svg width="7" height="7" viewBox="0 0 6 6"><path d="M2 1l2 2-2 2" stroke="#fff" stroke-width="1.3" fill="none"/></svg></span>Create a Free Profile</li>
      <li><span class="chev"><svg width="7" height="7" viewBox="0 0 6 6"><path d="M2 1l2 2-2 2" stroke="#fff" stroke-width="1.3" fill="none"/></svg></span>Find your Love</li>
    </ul>
  </div>
  <div class="abs col" style="left:676px;width:230px">
    <h2>Latest From Blog</h2>
    <div class="date">12 APRIL 2012</div>
    <p style="margin-bottom:24px">Nascetur ridiculus mus. Nulla dui. Fusce feugiat malesuada odio. Morbi nunc.</p>
    <div class="date">9 MARCH 2012</div>
    <p>Nascetur ridiculus mus. Nulla dui. Fusce feugiat malesuada odio. Morbi nunc.</p>
  </div>
  <a class="abs btn" style="left:104px">READ MORE <span class="chev" style="width:17px;height:17px"><svg width="7" height="7" viewBox="0 0 6 6"><path d="M2 1l2 2-2 2" stroke="#fff" stroke-width="1.3" fill="none"/></svg></span></a>
  <a class="abs btn" style="left:421px">READ MORE <span class="chev" style="width:17px;height:17px"><svg width="7" height="7" viewBox="0 0 6 6"><path d="M2 1l2 2-2 2" stroke="#fff" stroke-width="1.3" fill="none"/></svg></span></a>
  <a class="abs btn" style="left:677px">READ MORE <span class="chev" style="width:17px;height:17px"><svg width="7" height="7" viewBox="0 0 6 6"><path d="M2 1l2 2-2 2" stroke="#fff" stroke-width="1.3" fill="none"/></svg></span></a>
</main>

<div class="abs disclaimer">“We are not responsible for any sexually transmitted diseases" and " We are not responsible for any marriage break-ups or any problems in consequence after the encounters." "It is the responsibility of the subscriber(member) to have enough information about the person before the encounter."</div>

<footer>
  <div class="abs fcol" style="left:107px"><h3>About Us</h3><a href="#">Company Info</a><a href="#">Services</a><a href="#">Dating</a></div>
  <div class="abs fcol" style="left:299px;width:120px"><h3 style="margin-left:5px">Advice</h3><a href="#" style="padding-left:5px">FAQs</a><a href="#" style="padding-left:5px">Account</a><a href="#" style="padding-left:5px">Contacts</a></div>
  <div class="abs fcol" style="left:479px"><h3 style="margin-left:9px">Join In</h3><a href="#" style="padding-left:9px">Start Up</a><a href="#" style="padding-left:9px">Forums</a><a href="#" style="padding-left:9px">Promotions</a></div>
  <div class="abs social" aria-label="Social links"><span></span><span></span><span></span><span></span><span></span></div>
  <div class="abs fbrand">Amber Lanterns</div>
  <div class="abs copy">Copyright © 2012.&nbsp; All Rights Reserved.</div>
</footer>
</body>
</html>
```